Need a book cover design for a Vellora Book on Herbal Remedies

I need a book cover for my new ebook, here are the details:
Title: Meadow Tonics
Sub-Heading: Old Garden Wisdom Notes
Finding the Quiet Strength of the Wild for Daily Balance and Calm
Author: Mara Delacroix

```html
<!DOCTYPE html>
<html lang="en">
<head>
<meta charset="UTF-8">
<title>Meadow Tonics — Book Cover</title>
<link rel="stylesheet" href="https://fonts.googleapis.com/css2?family=Bebas+Neue&family=Oswald:wght@300&family=Poppins:wght@500;700;800&display=swap">
<style>
  :root {
    --canvas-bg: #ffffff;
    --cover-bg: #000000;
    --title-white: #fafafa;
    --title-lime: #b6c824;
    --photo-dark: #1c1d1e;
    --photo-mid: #4a4a48;
    --photo-wood: #6b4a30;
    --photo-cloth: #d9d9d6;
  }
  * { margin: 0; padding: 0; box-sizing: border-box; }
  html, body {
    width: 1200px;
    height: 2400px;
    overflow: hidden;
    background: var(--canvas-bg);
  }
  .book-cover {
    position: absolute;
    left: 180px;
    top: 528px;
    width: 840px;
    height: 1345px;
    background: var(--cover-bg);
    box-shadow: 0 6px 18px rgba(0,0,0,0.35);
    overflow: hidden;
  }
  .title {
    position: absolute;
    left: 0;
    width: 100%;
    text-align: center;
    font-family: "Bebas Neue", "Oswald", sans-serif;
    font-size: 300px;
    line-height: 1;
    letter-spacing: 2px;
    transform: scaleX(0.78);
    transform-origin: center top;
  }
  .title-line-one { top: 62px; color: var(--title-white); }
  .title-line-two { top: 300px; color: var(--title-lime); }
  .tagline {
    position: absolute;
    top: 542px;
    left: 0;
    width: 100%;
    text-align: center;
    font-family: "Oswald", sans-serif;
    font-weight: 300;
    font-size: 26px;
    letter-spacing: 16px;
    padding-left: 16px;
    color: var(--title-white);
    text-transform: uppercase;
  }
  .cover-photo {
    position: absolute;
    top: 595px;
    left: 0;
    width: 100%;
    height: 580px;
    background:
      radial-gradient(ellipse 45% 38% at 45% 58%, var(--photo-cloth) 0%, rgba(217,217,214,0.35) 40%, transparent 70%),
      radial-gradient(ellipse 60% 25% at 55% 85%, var(--photo-wood) 0%, transparent 75%),
      linear-gradient(180deg, var(--cover-bg) 0%, var(--photo-mid) 35%, var(--photo-dark) 80%, var(--cover-bg) 100%);
  }
  .blurb {
    position: absolute;
    top: 1182px;
    left: 0;
    width: 100%;
    text-align: center;
    font-family: "Poppins", sans-serif;
    color: var(--title-white);
    text-transform: uppercase;
    letter-spacing: 2px;
  }
  .blurb-line-one { font-weight: 700; font-size: 25px; line-height: 32px; }
  .blurb-line-two { font-weight: 500; font-size: 24px; line-height: 32px; }
  .author {
    position: absolute;
    top: 1262px;
    left: 0;
    width: 100%;
    text-align: center;
    font-family: "Poppins", sans-serif;
    font-weight: 800;
    font-size: 42px;
    letter-spacing: 7px;
    color: var(--title-lime);
    text-transform: uppercase;
  }
</style>
</head>
<body>
  <main class="book-cover">
    <h1>
      <span class="title title-line-one">Meadow</span>
      <span class="title title-line-two">Tonics</span>
    </h1>
    <p class="tagline">Old Garden Wisdom Notes</p>
    <div class="cover-photo" role="img" aria-label="Still life of herbal remedies: rolled white towel, herbal compress, oil dropper bottles, bowl of dried herbs and a glowing stone on dark wood"></div>
    <div class="blurb">
      <p class="blurb-line-one">Finding the Quiet Strength of the Wild</p>
      <p class="blurb-line-two">for Daily Balance &amp; Calm</p>
    </div>
    <p class="author">Mara Delacroix</p>
  </main>
</body>
</html>
```